Dental Business Card Design w/logo

Classic, elegant w/a touch of contemporary
Upscale dental facility located in Modesto CA
Specializing in restorative & general dentistry
Providing exceptional customer service to the community
Updates

I prefer script and not bold writing
If you can use the phone; fax and email icons instead of spelling them out, it would be great
No bold colors
Classy and elegant
In the back of the card I would like to see something like this
Your Next Appointment:
Mon     Tue    Wed    Thur (a box next to each of them for marking)
Date:_______________ at_____________ AM    PM  (a box next to them for marking)

Thank you

Target Market(s)

Well established professional

Industry/Entity Type

Dental

Contact Information for Business Card

Lavinteya Morbundi DMD
4176 Larkspur Rd
Suite F7
Modesto, CA 95355

Office: 209-731-5902
Fax: 209-731-8417
Email: morbundidmd@velmoranet.com

Requirements
Must have
• Unique classic logo
An easily repeatable design that can be used on letterhead and envelopes
Nice to have
• My initials incorporated into unique design
Should not have
• No cartoons or cheesy themes. This is a practice for the well established and professional individual.

```html
<!DOCTYPE html>
<html lang="en">
<head>
<meta charset="utf-8">
<title>Lavinteya Morbundi DMD – Business Card</title>
<link rel="stylesheet" href="https://fonts.googleapis.com/css2?family=PT+Sans:wght@400;700&display=swap">
<style>
  :root {
    --stage: #141414;
    --navy: #232a6e;
    --navy-deep: #1b2160;
    --cyan: #1fa3c9;
    --cyan-light: #8fd3e6;
    --paper: #ffffff;
    --ink: #1e2566;
    --back-ink: #e9ecff;
  }
  * { box-sizing: border-box; margin: 0; padding: 0; }
  html, body { width: 1200px; height: 900px; overflow: hidden; }
  body {
    background: var(--stage);
    font-family: "PT Sans", Arial, sans-serif;
    position: relative;
  }
  .card {
    position: absolute;
    top: 307px;
    width: 500px;
    height: 286px;
    border-radius: 18px;
    overflow: hidden;
  }
  /* Front */
  .card-front { left: 90px; background: var(--paper); color: var(--ink); }
  .holder {
    position: absolute; left: 34px; top: 44px;
  }
  .holder-name { font-size: 19px; color: var(--ink); margin-bottom: 8px; }
  .contact-list { list-style: none; font-size: 12.5px; line-height: 1.55; color: #1a1a2e; }
  .contact-list li { display: flex; align-items: center; gap: 7px; }
  .contact-list .icon { width: 12px; height: 12px; flex: none; }
  .contact-list .fx { font-size: 11px; color: var(--ink); width: 12px; flex: none; }
  .address { padding-left: 19px; }
  .brand {
    position: absolute; right: 32px; top: 62px;
    display: flex; align-items: center; gap: 10px;
  }
  .brand-dot { width: 14px; height: 14px; border-radius: 50%; background: var(--cyan); }
  .brand-name { font-size: 22px; color: var(--ink); line-height: 1.1; text-align: left; }
  .rule-light {
    position: absolute; left: 0; right: 0; top: 186px;
    height: 1px; background: var(--cyan-light);
  }
  .band-accent {
    position: absolute; left: 0; right: 0; bottom: 40px;
    height: 5px; background: var(--cyan);
  }
  .band-base {
    position: absolute; left: 0; right: 0; bottom: 0;
    height: 40px; background: var(--navy);
  }
  /* Back */
  .card-back {
    left: 610px; background: var(--navy);
    color: var(--back-ink);
    padding: 26px 34px;
    font-size: 12.5px; letter-spacing: 0.04em;
  }
  .form-line { height: 1px; background: rgba(233,236,255,0.75); }
  .form-heading { text-align: center; margin: 8px 0 8px; }
  .day-row { display: flex; justify-content: space-between; margin-bottom: 10px; }
  .day { display: flex; align-items: center; gap: 4px; }
  .box { width: 10px; height: 10px; background: var(--back-ink); display: inline-block; }
  .time-row { display: flex; align-items: flex-end; gap: 10px; margin-top: 12px; }
  .time-row .form-line { flex: 1; }
  .ampm { line-height: 1.1; font-size: 11.5px; }
  .notes-heading { text-align: center; margin: 10px 0 16px; }
  .notes .form-line { margin-bottom: 20px; }
</style>
</head>
<body>

<section class="card card-front" aria-label="Business card front">
  <div class="holder">
    <p class="holder-name">Lavinteya Morbundi</p>
    <ul class="contact-list">
      <li class="address">4176 Larkspur Rd Suite F7 Modesto, CA 95355</li>
      <li>
        <svg class="icon" viewBox="0 0 12 12" aria-label="Phone"><rect width="12" height="12" rx="2" fill="#1e2566"/><path d="M3.3 2.6c.4-.3.8-.2 1 .2l.6 1.1c.2.4.1.7-.2.9l-.4.3c.3.8.9 1.4 1.7 1.8l.3-.4c.2-.3.6-.4.9-.2l1.1.6c.4.2.5.6.2 1l-.5.6c-.3.3-.8.4-1.3.2C4.8 8.3 3.4 6.9 2.7 5c-.2-.5-.1-1 .2-1.3z" fill="#fff"/></svg>
        <span>209-731-5902</span>
      </li>
      <li><span class="fx">Fx</span><span>209-731-8417</span></li>
      <li>
        <svg class="icon" viewBox="0 0 12 12" aria-label="Email"><rect y="2" width="12" height="8" rx="1" fill="#1e2566"/><path d="M1 3l5 3.5L11 3" stroke="#fff" stroke-width="1" fill="none"/></svg>
        <span>morbundidmd@velmoranet.com</span>
      </li>
    </ul>
  </div>

  <div class="brand">
    <span class="brand-dot"></span>
    <p class="brand-name">Lavinteya<br>Morbundi DMD</p>
  </div>

  <div class="rule-light"></div>
  <div class="band-accent"></div>
  <div class="band-base"></div>
</section>

<section class="card card-back" aria-label="Business card back, appointment form">
  <div class="form-line"></div>
  <p class="form-heading">HAS AN APPOINTMENT ON</p>
  <div class="day-row">
    <span class="day"><i class="box"></i>MON.</span>
    <span class="day"><i class="box"></i>TUES.</span>
    <span class="day"><i class="box"></i>WED.</span>
    <span class="day"><i class="box"></i>THURS.</span>
    <span class="day"><i class="box"></i>FRI.</span>
    <span class="day"><i class="box"></i>SAT</span>
  </div>
  <div class="form-line"></div>
  <div class="time-row">
    <div class="form-line"></div>
    <span>AT</span>
    <div class="form-line"></div>
    <span class="ampm">A.M<br>P.M</span>
  </div>
  <p class="notes-heading">THINGS TO ASK MY DENTIST</p>
  <div class="notes">
    <div class="form-line"></div>
    <div class="form-line"></div>
  </div>
</section>

</body>
</html>
```